Copyright Registration Service Website

Rightsbloomery.com (site can be accessed) is a website that will enable artists, photographers, writers, sculptors, musicians and other creative persons of all media to register their works of authorship with the U.S. Hall of Registers, Filing Bureau, for a nominal fee of $99 plus filing fees (in most cases). The high points of marketing are (1) every application is reviewed by a lawyer and (2) the entire copyright process is monitored, as part of the service fee. There are 8 categories of copyrightability:
Literary Works
Dramatic Works
Musical Works
Sound Recordings
Motion Pictures
Choreographic and Pantomime Works
Photographs, Paintings and Sculptures
Architectural Works
Please look at the existing site; provide a better landing page than currently exists. In particular, the logo is in need of serious improvement. We would like it to be bright and sunny; visually pleasant and witty; and clever but not "doctoral" in presentation. Thank you for your participation.

Target Market(s)

photographers, artists, musicians, age groups of 20-50

Industry/Entity Type

Marketing

Requirements
Should not have
• stiffness

```html
<!DOCTYPE html>
<html lang="en">
<head>
<meta charset="utf-8">
<title>Rightsbloomery.com – Copyright Registration</title>
<link rel="stylesheet" href="https://fonts.googleapis.com/css2?family=Signika:wght@400;600;700&family=Arimo:wght@400;700&display=swap">
<style>
:root{
  --blue:#0f8ed6;
  --blue-dark:#0a74b5;
  --ink:#222;
  --grey:#5b6368;
  --hero:#1c2226;
  --paper:#ececec;
  --card:#f1f1f1;
  --footer:#1e1e1e;
  --footer-box:#3b3b3b;
  --white:#fff;
}
*{margin:0;padding:0;box-sizing:border-box}
html,body{width:1154px;height:1200px;overflow:hidden;background:var(--white)}
body{position:relative;font-family:Arimo,Arial,sans-serif;color:var(--ink)}
.abs{position:absolute}

/* header */
.topline{left:0;top:0;width:1154px;height:3px;background:#2a2a2a}
.brand{left:99px;top:14px;display:flex;align-items:center;gap:8px}
.brand-dot{width:58px;height:58px;border-radius:50%;border:3px solid #222;background:var(--white)}
.brand-name{font-family:Signika,sans-serif;font-weight:700;font-size:24px;letter-spacing:.3px;color:#1b1b1b;line-height:1}
.brand-url{font-family:Arimo,sans-serif;font-size:12px;color:#555;margin-top:5px;text-align:right}
.account{left:901px;top:3px;width:155px;height:29px;background:#222;border-radius:0 0 9px 9px;color:var(--white);font-family:Signika,sans-serif;font-size:13.5px;display:flex;align-items:center;justify-content:center;gap:8px}

.nav{left:98px;top:92px;width:958px;height:36px;background:var(--blue);display:flex}
.nav a{color:var(--white);text-decoration:none;font-family:Signika,sans-serif;font-size:14px;display:flex;align-items:center;justify-content:center;border-right:1px solid #3ba4e0}
.nav a:last-child{border-right:0}

/* hero */
.hero{left:0;top:130px;width:1154px;height:450px;background:radial-gradient(ellipse at 50% 40%,#263036 0%,var(--hero) 70%,#161b1e 100%)}
.hero-title{top:25px;left:0;width:100%;text-align:center;font-family:Signika,sans-serif;font-weight:700;font-size:22px;color:var(--blue);letter-spacing:.2px}
.hero-sub{top:57px;left:0;width:100%;text-align:center;font-family:Signika,sans-serif;font-size:20px;color:#5d666b;letter-spacing:.3px}
.frame{background:var(--white);border-radius:4px;padding:6px;box-shadow:0 4px 14px rgba(0,0,0,.5)}
.frame .fill{width:100%;height:100%}
.slide-label{font-family:Signika,sans-serif;color:var(--white);font-size:12.5px;white-space:nowrap}
.arrow{width:41px;height:41px;border-radius:5px;background:linear-gradient(#d6d6d6,#8f8f8f);display:flex;align-items:center;justify-content:center;box-shadow:0 2px 4px rgba(0,0,0,.5)}

/* welcome */
.welcome{left:0;top:580px;width:1154px;height:171px;background:linear-gradient(#ededed,#e4e4e4)}
.welcome h1{position:absolute;top:15px;width:100%;text-align:center;font-family:Signika,sans-serif;font-weight:400;font-size:23px;color:#333}
.welcome h1 span{color:var(--blue)}
.welcome .ask{position:absolute;top:57px;width:100%;text-align:center;font-weight:700;font-size:12px}
.welcome p.lead{position:absolute;top:86px;left:105px;width:946px;font-size:12px;line-height:19.5px;text-align:justify;text-align-last:center;color:#333}

/* features */
.features{left:0;top:751px;width:1154px;height:341px;background:var(--card)}
.card{top:40px;width:227px;height:281px;background:#f3f3f3;border:1px solid #dadada}
.card.active{background:var(--blue);border-color:var(--blue-dark)}
.card .badge{position:absolute;left:50%;top:-24px;margin-left:-24px;width:48px;height:48px;border-radius:50%;background:radial-gradient(circle at 40% 35%,#6a6a6a,#2c2c2c);border:2px solid #cfcfcf;display:flex;align-items:center;justify-content:center}
.card .pic{position:absolute;left:9px;top:26px;width:208px;height:113px}
.card.active .pic{border:3px solid var(--white)}
.card h2{position:absolute;left:10px;top:157px;font-family:Signika,sans-serif;font-weight:600;font-size:20px;letter-spacing:.5px;color:#3a3a3a}
.card.active h2{color:var(--white)}
.card p{position:absolute;left:13px;top:189px;width:204px;font-size:12px;line-height:17.5px;text-align:justify;color:#555}
.card.active p{color:var(--white)}
.card .more{position:absolute;right:10px;bottom:6px;font-weight:700;font-size:12px;color:#333}
.card.active .more{color:var(--white)}

/* footer */
.footer{left:0;top:1092px;width:1154px;height:108px;background:var(--footer)}
.foot-links{left:101px;top:12px;font-family:Signika,sans-serif;font-size:12px;color:#e5e5e5;display:flex;gap:9px}
.foot-links span.sep{color:#aaa}
.foot-copy{right:98px;top:12px;font-family:Signika,sans-serif;font-size:12px;color:#e5e5e5}
.disclaimer{left:98px;top:37px;width:958px;height:60px;background:var(--footer-box);padding:7px 15px;font-family:Signika,sans-serif;font-size:11.5px;line-height:15.5px;color:#d8d8d8}
.disclaimer b{color:#eee}
</style>
</head>
<body>

<div class="abs topline"></div>

<div class="abs brand">
  <div class="brand-dot"></div>
  <div>
    <div class="brand-name">RIGHTSBLOOMERY</div>
    <div class="brand-url">RIGHTSBLOOMERY.COM</div>
  </div>
</div>

<div class="abs account"><span>My account</span><span>|</span><span>Login</span></div>

<nav class="abs nav">
  <a style="width:113px">About Us</a>
  <a style="width:219px">Copyright Cateogries</a>
  <a style="width:204px">Law &amp; Statutes</a>
  <a style="width:194px">Copyright Process</a>
  <a style="width:139px">Contact Us</a>
  <a style="width:89px">Links</a>
</nav>

<section class="abs hero">
  <div class="abs hero-title">EVERY APPLICATION IS INDIVIDUALLY FILED AND MONITORED UNDER LAWYER SUPERVISION.</div>
  <div class="abs hero-sub">PROTECT YOUR INTELLECTUAL PROPERTY RIGHTS</div>

  <div class="abs slide-label" style="left:147px;top:316px">Musical works</div>
  <div class="abs slide-label" style="left:917px;top:316px">Motion pictures</div>

  <div class="abs frame" style="left:134px;top:199px;width:78px;height:111px">
    <div class="fill" role="img" aria-label="Musician playing a guitar" style="background:linear-gradient(135deg,#c9c9c9,#8a8a8a)"></div>
  </div>
  <div class="abs frame" style="left:907px;top:199px;width:105px;height:111px">
    <div class="fill" role="img" aria-label="Film studio set with lights" style="background:linear-gradient(135deg,#f2f2f2,#cfcfcf)"></div>
  </div>

  <div class="abs slide-label" style="left:245px;top:338px;font-size:13px">Literary works</div>
  <div class="abs slide-label" style="left:808px;top:338px;font-size:13px">Sound Rcording</div>

  <div class="abs frame" style="left:207px;top:174px;width:115px;height:160px">
    <div class="fill" role="img" aria-label="Stack of old leather-bound books" style="background:linear-gradient(90deg,#3a2a1e,#8c6a45 40%,#5a3e28)"></div>
  </div>
  <div class="abs frame" style="left:798px;top:174px;width:114px;height:160px">
    <div class="fill" role="img" aria-label="Person wearing studio headphones" style="background:linear-gradient(135deg,#6b6b6b,#3a3a3a)"></div>
  </div>

  <div class="abs frame" style="left:316px;top:107px;width:488px;height:274px">
    <div class="fill" role="img" aria-label="Painting of a figure leaping across a glowing sea" style="background:linear-gradient(120deg,#40606a 0%,#8aa3a0 35%,#e8c860 60%,#9b7a30 80%,#2c3a3c 100%)"></div>
  </div>
  <div class="abs slide-label" style="left:0;width:1141px;text-align:center;top:389px;font-size:17px">Visual Art Work</div>

  <div class="abs arrow" style="left:78px;top:235px">
    <svg width="26" height="20" viewBox="0 0 26 20"><path d="M1 10 L11 1 V6 H25 V14 H11 V19 Z" fill="#1e1e1e"/></svg>
  </div>
  <div class="abs arrow" style="left:1020px;top:235px">
    <svg width="26" height="20" viewBox="0 0 26 20"><path d="M25 10 L15 1 V6 H1 V14 H15 V19 Z" fill="#1e1e1e"/></svg>
  </div>
</section>

<section class="abs welcome">
  <h1>Welcome To Rights <span>BLOOMERY</span></h1>
  <div class="ask">Are you an artist or otherwise engaged in a creative field?</div>
  <p class="lead">In the modern age, it is vital to protect your artistic, intellectual and moral rights that exist in your works of authorship.&nbsp; The United States Copyright Act of 1976, as amended, provides protection for such works of authorship that are fixed in a tangible medium of expression.&nbsp; Once a copyright registration is created, it protects your creative authorship forever, with your artistic expression being preserved forever in the U.S. Hall of Registers in Washington, DC.</p>
</section>

<section class="abs features">
  <article class="abs card active" style="left:101px">
    <div class="badge"><span style="color:#fff;font-size:38px;line-height:1;font-family:Arimo,sans-serif">©</span></div>
    <div class="pic" role="img" aria-label="Hand pressing a copyright rubber stamp" style="background:linear-gradient(135deg,#8aa0b8,#d8d8d8 55%,#c2a070)"></div>
    <h2>Copyright Cateogries</h2>
    <p>Lorem ipsum dolor sit amet, consectetuer adipiscing elit, sed diam nonummy nibh euismod tincidunt ut laoreet dolore …</p>
    <div class="more">Moreinfo</div>
  </article>

  <article class="abs card" style="left:344px">
    <div class="badge">
      <svg width="30" height="26" viewBox="0 0 30 26" fill="none" stroke="#fff" stroke-width="1.6"><path d="M15 2V23M8 23H22M4 5H26M4 5L1 14H7ZM26 5L23 14H29Z"/><path d="M1 14Q4 18 7 14M23 14Q26 18 29 14"/></svg>
    </div>
    <div class="pic" role="img" aria-label="Judge's gavel beside brass scales" style="background:linear-gradient(135deg,#d2601a,#7a2a08 55%,#3a1a08)"></div>
    <h2>LAW &amp; STATUTES</h2>
    <p>Lorem ipsum dolor sit amet, consectetuer adipiscing elit, sed diam nonummy nibh euismod tincidunt ut laoreet dolore …</p>
    <div class="more">Moreinfo</div>
  </article>

  <article class="abs card" style="left:589px">
    <div class="badge">
      <svg width="26" height="26" viewBox="0 0 26 26" fill="#fff"><circle cx="13" cy="8" r="6"/><path d="M2 25C2 18 7 15 13 15S24 18 24 25Z"/></svg>
    </div>
    <div class="pic" role="img" aria-label="Two business people shaking hands" style="background:linear-gradient(90deg,#2a2a2e,#d8d8d8 50%,#2e2e30)"></div>
    <h2>ABOUT US</h2>
    <p>Lorem ipsum dolor sit amet, consectetuer adipiscing elit, sed diam nonummy nibh euismod tincidunt ut laoreet dolore …</p>
    <div class="more">Moreinfo</div>
  </article>

  <article class="abs card" style="left:832px">
    <div class="badge">
      <svg width="34" height="34" viewBox="0 0 34 34" fill="none" stroke="#fff" stroke-width="2.4"><circle cx="17" cy="17" r="15"/><path d="M12 13Q12 8 17 8T22 13Q22 16 17 18V21"/><circle cx="17" cy="26" r="1" fill="#fff"/></svg>
    </div>
    <div class="pic" role="img" aria-label="Signpost with question words against a blue sky" style="background:linear-gradient(#2f6ed0,#6aa0e6 60%,#dfe9f6)"></div>
    <h2>FAQs</h2>
    <p>Lorem ipsum dolor sit amet, consectetuer adipiscing elit, sed diam nonummy nibh euismod tincidunt ut laoreet dolore …</p>
    <div class="more">Moreinfo</div>
  </article>
</section>

<footer class="abs footer">
  <div class="abs foot-links">
    <span>ABOUT US</span><span class="sep">|</span>
    <span>CUSTOMER SERVICE</span><span class="sep">|</span>
    <span>PRIVACY POLICY</span><span class="sep">|</span>
    <span>CONTACT US</span>
  </div>
  <div class="abs foot-copy">© 2013 Rightsbloomery.com. All Rights Reserved.</div>
  <div class="abs disclaimer"><b>Disclaimer :</b> Lorem ipsum dolor sit amet, consectetuer adipiscing elit. Morbi luctus. Duis lobortis. Nulla nec velit. Mauris pulvinar erat non massa. Suspendisse tortor turpis, porta nec, tempus vitae, iaculis semper, pede. Cras vel libero id lectus rhoncus porta. Suspendisse convallis felis ac enim. Vivamus tortor nisl, lobortis in, faucibus et, tempus at, dui. Nunc risus. Proin scelerisque augue. Nam ullamcorper.</div>
</footer>

</body>
</html>
```